Customer Dashboard Design for Email Security SaaS

Mailbrook is a commercial email spam filter offered as a SaaS product, built and operated by a small German hosting provider. It protects business email accounts against spam, phishing, scam, and viruses using a multilayer filtering pipeline that combines traditional spam detection with AI-powered classification. The product runs entirely on German infrastructure, ensuring data sovereignty for European customers.

We need a complete redesign of the customer-facing dashboard. This is the web application where paying customers manage their email filtering: view their mail log, check quarantined emails, manage allow/blocklists, configure their settings, and handle their subscription. It is the primary touchpoint between Mailbrook and its customers.

Our customers are system administrators, IT managers at small-to-medium businesses, and operators of small hosting providers. They are technically competent but not designers. They expect professional, efficient tools that respect their time. They typically manage 10–500 email accounts and check the dashboard a few times per week, with heavier use during spam incidents.

We have attached the current mockups which really need to be replaced with something good looking.

Target Market(s)

System administrators, IT managers at small-to-medium businesses, and operators of small hosting providers.

Industry/Entity Type

SaaS

Number of Pages Required

5+ page

```html
<!DOCTYPE html>
<html lang="de">
<head>
<meta charset="utf-8">
<title>Mailbrook – Kunden-Dashboard</title>
<link href="https://fonts.googleapis.com/css2?family=Inter:wght@400;500;600;700&display=swap" rel="stylesheet">
<style>
:root{
  --page:#9a9a9a;
  --panel:#0c0c0c;
  --side:#0a0a0a;
  --card:#151515;
  --card-2:#1b1b1b;
  --line:#262626;
  --line-soft:#1f1f1f;
  --text:#ececec;
  --muted:#9a9a9a;
  --dim:#6a6a6a;
  --green:#1f8a5f;
  --green-hi:#2fcf8c;
  --green-deep:#0f3d2b;
  --red:#b3262a;
  --ham:#22c55e;
  --spam:#e0302f;
  --phish:#e59a12;
  --virus:#3b9be8;
}
*{box-sizing:border-box;margin:0;padding:0}
html,body{width:1200px;height:406px;overflow:hidden;background:var(--page)}
body{font-family:"Inter",sans-serif;color:var(--text)}
.stage{position:absolute;left:0;top:0;width:2576px;height:871px;transform:scale(.46584);transform-origin:0 0}
.panel{position:absolute;top:84px;width:809px;background:var(--panel);overflow:hidden}
.panel--dash{left:35px;height:726px}
.panel--log{left:873px;height:521px}
.panel--quar{left:1711px;height:521px}
.abs{position:absolute}

/* header */
.topbar{position:absolute;left:0;top:0;width:809px;height:42px;border-bottom:1px solid var(--line-soft)}
.brand{position:absolute;left:12px;top:12px;display:flex;align-items:center;gap:8px;font-weight:700;font-size:9px}
.brand-dot{width:18px;height:18px;border-radius:50%;background:var(--green)}
.greet{position:absolute;left:150px;top:11px}
.greet h2{font-size:8.5px;font-weight:700}
.greet p{font-size:5px;color:var(--muted);margin-top:3px}
.tools{position:absolute;right:18px;top:8px;display:flex;align-items:center;gap:10px}
.tool{width:20px;height:20px;position:relative}
.avatar{width:27px;height:27px;border-radius:50%;background:radial-gradient(circle at 50% 40%,#c98b62,#6b3f28)}
.user{font-size:7px;display:flex;align-items:center;gap:6px}
/* sidebar */
.sidebar{position:absolute;left:0;top:42px;width:130px;bottom:0;background:var(--side);border-right:1px solid var(--line-soft)}
.nav{list-style:none;margin-top:14px}
.nav li{height:22.5px;display:flex;align-items:center;gap:7px;padding-left:12px;font-size:6.5px;color:#d8d8d8}
.nav li svg{width:8px;height:8px}
.nav li.is-active{color:var(--green-hi);background:linear-gradient(90deg,#0f2219,transparent)}
/* cards */
.card{position:absolute;background:var(--card);border:1px solid var(--line);border-radius:8px;overflow:hidden}
.card--accent{border-bottom:2px solid var(--green)}
.ico-box{width:16px;height:16px;border-radius:4px;background:var(--green-deep);border:1px solid #1e6a4a;display:flex;align-items:center;justify-content:center}
.stat-label{position:absolute;left:12px;top:12px;display:flex;align-items:center;gap:8px;font-size:8px;letter-spacing:.06em;font-weight:500}
.stat-num{position:absolute;left:12px;top:40px;font-size:24px;font-weight:700;letter-spacing:-.02em}
.stat-cap{position:absolute;left:12px;top:80px;font-size:6.5px;color:#cfcfcf}
.btn{position:absolute;display:flex;align-items:center;justify-content:center;border-radius:3px;font-size:7px;color:#fff;background:var(--green);gap:4px}
.btn--dark{background:#1e1e1e;border:1px solid var(--line)}
.btn--red{background:var(--red)}
.page-title{position:absolute;left:150px;top:56px;font-size:12px;font-weight:400;letter-spacing:-.01em}
.page-desc{position:absolute;left:150px;top:76px;font-size:7px;line-height:14px;color:#bdbdbd;width:330px}
/* table */
.log-table{position:absolute;left:12px;top:9px;width:616px;border-collapse:collapse;table-layout:fixed;font-size:6.5px}
.log-table th,.log-table td{border:1px solid var(--line);padding:0 10px;text-align:left;height:33.7px}
.log-table th{font-weight:600;font-size:8px}
.verdict{display:flex;justify-content:space-between;align-items:center}
.v-ham{color:var(--ham)}.v-spam{color:var(--spam)}.v-phish{color:var(--phish)}.v-virus{color:var(--virus)}
.field-label{position:absolute;top:13px;font-size:4.5px;letter-spacing:.1em;color:var(--dim)}
.field{position:absolute;top:24px;height:21px;background:#1f1f1f;border:1px solid var(--line);border-radius:3px;font-size:6.5px;display:flex;align-items:center;padding:0 7px;gap:5px}
.pager{position:absolute;right:14px;top:8px;display:flex;gap:6px;align-items:center;font-size:7.5px;color:#cfcfcf}
.pager span{padding:4px 6px}
.pager .cur{background:var(--green);color:#fff;border-radius:2px}
/* quarantine */
.q-card .mail{position:absolute;left:12px;top:16px;font-size:8.5px}
.q-card .pill{position:absolute;right:12px;top:12px;height:20px;padding:0 10px;border-radius:3px;background:#1e1e1e;border:1px solid var(--line);font-size:6.5px;display:flex;align-items:center;gap:5px}
.q-card .rule{position:absolute;left:12px;right:12px;height:1px;background:var(--line)}
.q-card .subj{position:absolute;left:12px;top:52px;font-size:9.5px;font-weight:600}
.q-card .meta{position:absolute;left:12px;right:12px;top:81px;font-size:6.5px;display:flex;justify-content:space-between}
.check{position:absolute;width:9px;height:9px;border:1px solid #555;border-radius:2px}
.tool-item{display:flex;align-items:center;gap:4px}
.sys-pill{position:absolute;right:12px;top:36px;font-size:4.5px;color:var(--green-hi);border:1px solid #1e6a4a;border-radius:8px;padding:2px 7px;background:#0e2419}
</style>
</head>
<body>
<div class="stage">

<!-- ================= DASHBOARD ================= -->
<section class="panel panel--dash">
  <header class="topbar">
    <div class="brand"><span class="brand-dot"></span>Mailbrook</div>
    <div class="greet"><h2>Guten Tag, Lena Maurer</h2><p>Beobachtungsmodus - Mails werden analysiert aber nicht blockiert</p></div>
    <div class="tools">
      <svg class="tool" viewBox="0 0 20 20"><circle cx="10" cy="10" r="9" fill="#eee"/><circle cx="6" cy="10" r="1.3" fill="#111"/><circle cx="10" cy="10" r="1.3" fill="#111"/><circle cx="14" cy="10" r="1.3" fill="#111"/></svg>
      <svg class="tool" viewBox="0 0 20 20"><path d="M5 15h10l-1.5-2V9a3.5 3.5 0 0 0-7 0v4z" fill="none" stroke="#eee" stroke-width="1.6"/><circle cx="15" cy="5" r="4" fill="var(--green)"/></svg>
      <div class="avatar" role="img" aria-label="Profilfoto des Benutzers"></div>
      <div class="user">Lena Maurer <svg width="6" height="6" viewBox="0 0 6 6"><path d="M1 2l2 2 2-2" stroke="#eee" fill="none"/></svg></div>
    </div>
  </header>
  <aside class="sidebar">
    <ul class="nav">
      <li class="is-active"><svg viewBox="0 0 8 8"><rect x="0" y="0" width="3" height="3" fill="currentColor"/><rect x="5" y="0" width="3" height="3" fill="currentColor"/><rect x="0" y="5" width="3" height="3" fill="currentColor"/><rect x="5" y="5" width="3" height="3" fill="currentColor"/></svg>Dashboard</li>
      <li><svg viewBox="0 0 8 8"><path d="M0 1h8M0 4h8M0 7h8" stroke="currentColor"/></svg>Mail-Log</li>
      <li><svg viewBox="0 0 8 8"><path d="M4 .5l3 1.2v2.6C7 6 5.5 7.2 4 7.6 2.5 7.2 1 6 1 4.3V1.7z" fill="none" stroke="currentColor"/></svg>Quarantine</li>
      <li><svg viewBox="0 0 8 8"><rect x=".5" y="1.5" width="7" height="5" fill="none" stroke="currentColor"/></svg>Mailbox Quota</li>
      <li><svg viewBox="0 0 8 8"><circle cx="4" cy="4" r="3" fill="none" stroke="currentColor"/><circle cx="4" cy="4" r="1" fill="currentColor"/></svg>Settings</li>
      <li><svg viewBox="0 0 8 8"><rect x="1.5" y="3.5" width="5" height="4" fill="none" stroke="currentColor"/><path d="M2.5 3.5V2a1.5 1.5 0 0 1 3 0v1.5" fill="none" stroke="currentColor"/></svg>Paywall Overlay</li>
      <li><svg viewBox="0 0 8 8"><rect x=".5" y=".5" width="7" height="7" fill="none" stroke="currentColor"/><path d="M3 .5v7" stroke="currentColor"/></svg>Navigation Shell</li>
    </ul>
  </aside>

  <div class="card card--accent" style="left:150px;top:54px;width:207px;height:101px">
    <div class="stat-label"><span class="ico-box"><svg width="8" height="8" viewBox="0 0 8 8"><path d="M4 .5l3 1.2v2.6C7 6 5.5 7.2 4 7.6 2.5 7.2 1 6 1 4.3V1.7z" fill="none" stroke="var(--green-hi)"/></svg></span>SPAM &amp; BEDROHUNGEN</div>
    <div class="stat-num">4,202</div>
    <div class="stat-cap">Spam, Phishing und Viren erfolgreich blockiert</div>
  </div>
  <div class="card card--accent" style="left:366px;top:54px;width:208px;height:101px">
    <div class="stat-label"><span class="ico-box"><svg width="8" height="8" viewBox="0 0 8 8"><rect x=".5" y="1.5" width="7" height="5" fill="none" stroke="var(--green-hi)"/></svg></span>NEWSLETTER &amp; SONSTIGES</div>
    <div class="stat-num">2,100</div>
    <div class="stat-cap">Automatisch kategorisierte E-Mails</div>
  </div>
  <div class="card card--accent" style="left:583px;top:54px;width:207px;height:101px">
    <div class="stat-label"><span class="ico-box"><svg width="8" height="8" viewBox="0 0 8 8"><path d="M4 1l3.2 6H.8z" fill="none" stroke="var(--green-hi)"/></svg></span>IN QUARANTÄNE</div>
    <div class="stat-num">56</div>
    <div class="stat-cap">Zur Überprüfung bereit</div>
  </div>

  <div class="card" style="left:150px;top:167px;width:640px;height:316px">
    <div class="abs" style="left:12px;top:12px;font-size:8.5px;font-weight:700">E-Mail Aktivität</div>
    <div class="abs" style="left:12px;top:26px;font-size:4.5px;color:var(--muted)">Letzte 7 / 30 Tage</div>
    <div class="abs" style="right:12px;top:12px;height:23px;padding:0 10px;border:1px solid var(--line);border-radius:3px;background:#111;font-size:6px;display:flex;align-items:center;gap:6px">Letzte 30 Tage <svg width="6" height="6" viewBox="0 0 6 6"><path d="M1 2l2 2 2-2" stroke="#eee" fill="none"/></svg></div>
    <svg class="abs" style="left:0;top:0" width="640" height="316" viewBox="0 0 640 316">
      <defs>
        <linearGradient id="areaFill" x1="0" y1="0" x2="0" y2="1">
          <stop offset="0" stop-color="#1f8a5f" stop-opacity=".75"/>
          <stop offset="1" stop-color="#1f8a5f" stop-opacity=".05"/>
        </linearGradient>
      </defs>
      <g stroke="#2c2c2c" stroke-dasharray="4 4" stroke-width=".8">
        <path d="M45 53H630M45 90H630M45 125H630M45 161H630M45 197H630M45 234H630M45 270H630"/>
      </g>
      <g fill="#d8d8d8" font-family="Inter,sans-serif" font-size="10">
        <text x="12" y="57">1000</text><text x="12" y="94">800</text><text x="12" y="129">600</text><text x="12" y="165">450</text><text x="12" y="201">300</text><text x="12" y="238">150</text><text x="12" y="274">0</text>
      </g>
      <path d="M47,161 Q73,154 84,164 Q95,174 110,195 Q125,216 140,210 Q155,204 172.5,186.5 Q190,169 205,143 Q220,117 232.5,128 Q245,139 257.5,146.5 Q270,154 282.5,148 Q295,142 312.5,150.5 Q330,159 345,174 Q360,189 375,179 Q390,169 402.5,149 Q415,129 430,108 Q445,87 457.5,95.5 Q470,104 487.5,131.5 Q505,159 520,171.5 Q535,184 550,172.5 Q565,161 575,146 Q585,131 595,120 Q605,109 627,62 L627,270 L47,270 Z" fill="url(#areaFill)"/>
      <path d="M47,161 Q73,154 84,164 Q95,174 110,195 Q125,216 140,210 Q155,204 172.5,186.5 Q190,169 205,143 Q220,117 232.5,128 Q245,139 257.5,146.5 Q270,154 282.5,148 Q295,142 312.5,150.5 Q330,159 345,174 Q360,189 375,179 Q390,169 402.5,149 Q415,129 430,108 Q445,87 457.5,95.5 Q470,104 487.5,131.5 Q505,159 520,171.5 Q535,184 550,172.5 Q565,161 575,146 Q585,131 595,120 Q605,109 627,62" fill="none" stroke="#26b57a" stroke-width="2.5"/>
      <g fill="#bdbdbd" font-family="Inter,sans-serif" font-size="9" text-anchor="middle">
        <text x="54" y="297">Jan 23</text><text x="103" y="297">Feb 23</text><text x="154" y="297">Mar 14</text><text x="202" y="297">Apr 23</text><text x="254" y="297">May 23</text><text x="306" y="297">Jun 23</text><text x="355" y="297">Jul 23</text><text x="403" y="297">Aug 23</text><text x="456" y="297">Sept 23</text><text x="508" y="297">Oct 23</text><text x="559" y="297">Nov 23</text><text x="610" y="297">Dec 23</text>
      </g>
    </svg>
  </div>

  <div class="card card--accent" style="left:150px;top:495px;width:315px;height:134px">
    <div class="abs ico-box" style="left:12px;top:12px"><svg width="8" height="8" viewBox="0 0 8 8"><rect x="1.5" y="3.5" width="5" height="4" fill="none" stroke="var(--green-hi)"/></svg></div>
    <div class="abs" role="img" aria-label="Dekoratives Schild-Symbol" style="left:195px;top:18px;width:96px;height:96px;border-radius:50%;background:radial-gradient(circle,#2a2a2a,transparent 70%)"></div>
    <div class="abs" style="left:12px;top:43px;font-size:12.5px;font-weight:700">Quarantäne prüfen</div>
    <div class="abs" style="left:12px;top:64px;font-size:6.5px;line-height:9px;width:160px">Überprüfen Sie zurückgehaltene E-Mails und geben Sie diese bei Bedarf frei.</div>
    <div class="btn" style="left:12px;top:96px;width:109px;height:27px;font-size:7.5px">Zur Quarantäne</div>
  </div>
  <div class="card card--accent" style="left:475px;top:495px;width:315px;height:134px">
    <div class="abs ico-box" style="left:12px;top:12px"><svg width="8" height="8" viewBox="0 0 8 8"><rect x=".5" y="1.5" width="7" height="5" fill="none" stroke="var(--green-hi)"/></svg></div>
    <div class="abs" role="img" aria-label="Dekorative Brief- und Dokument-Illustration" style="left:192px;top:22px;width:100px;height:88px;border-radius:50%;background:radial-gradient(circle,#2a2a2a,transparent 70%)"></div>
    <div class="abs" style="left:12px;top:43px;font-size:12.5px;font-weight:700">Mail-Log anzeigen</div>
    <div class="abs" style="left:12px;top:64px;font-size:6.5px;line-height:9px;width:160px">Sehen Sie alle verarbeiteten E-Mails und deren Status im Detail ein.</div>
    <div class="btn" style="left:12px;top:96px;width:111px;height:27px;font-size:7.5px">Mail-Log Öffnen</div>
  </div>

  <div class="card card--accent" style="left:150px;top:643px;width:640px;height:66px">
    <div class="abs" style="left:12px;top:17px;font-size:12.5px;font-weight:700">Systemstatus</div>
    <div class="abs" style="left:12px;top:40px;font-size:6.5px">Alle Filter arbeiten einwandfrei. Letztes Update: 12.05.2024,14:32 Uhr</div>
    <div class="sys-pill">Alle Systeme aktiv</div>
  </div>
</section>

<!-- ================= MAIL-LOG ================= -->
<section class="panel panel--log">
  <header class="topbar">
    <div class="brand"><span class="brand-dot"></span>Mailbrook</div>
    <div class="greet"><h2>Guten Tag, Lena Maurer</h2><p>Beobachtungsmodus - Mails werden analysiert aber nicht blockiert</p></div>
    <div class="tools">
      <svg class="tool" viewBox="0 0 20 20"><circle cx="10" cy="10" r="9" fill="#eee"/><circle cx="6" cy="10" r="1.3" fill="#111"/><circle cx="10" cy="10" r="1.3" fill="#111"/><circle cx="14" cy="10" r="1.3" fill="#111"/></svg>
      <svg class="tool" viewBox="0 0 20 20"><path d="M5 15h10l-1.5-2V9a3.5 3.5 0 0 0-7 0v4z" fill="none" stroke="#eee" stroke-width="1.6"/><circle cx="15" cy="5" r="4" fill="var(--green)"/></svg>
      <div class="avatar" role="img" aria-label="Profilfoto des Benutzers"></div>
      <div class="user">Lena Maurer <svg width="6" height="6" viewBox="0 0 6 6"><path d="M1 2l2 2 2-2" stroke="#eee" fill="none"/></svg></div>
    </div>
  </header>
  <aside class="sidebar">
    <ul class="nav">
      <li><svg viewBox="0 0 8 8"><rect x="0" y="0" width="3" height="3" fill="currentColor"/><rect x="5" y="0" width="3" height="3" fill="currentColor"/><rect x="0" y="5" width="3" height="3" fill="currentColor"/><rect x="5" y="5" width="3" height="3" fill="currentColor"/></svg>Dashboard</li>
      <li class="is-active"><svg viewBox="0 0 8 8"><path d="M0 1h8M0 4h8M0 7h8" stroke="currentColor"/></svg>Mail-Log</li>
      <li><svg viewBox="0 0 8 8"><path d="M4 .5l3 1.2v2.6C7 6 5.5 7.2 4 7.6 2.5 7.2 1 6 1 4.3V1.7z" fill="none" stroke="currentColor"/></svg>Quarantine</li>
      <li><svg viewBox="0 0 8 8"><rect x=".5" y="1.5" width="7" height="5" fill="none" stroke="currentColor"/></svg>Mailbox Quota</li>
      <li><svg viewBox="0 0 8 8"><circle cx="4" cy="4" r="3" fill="none" stroke="currentColor"/><circle cx="4" cy="4" r="1" fill="currentColor"/></svg>Settings</li>
      <li><svg viewBox="0 0 8 8"><rect x="1.5" y="3.5" width="5" height="4" fill="none" stroke="currentColor"/><path d="M2.5 3.5V2a1.5 1.5 0 0 1 3 0v1.5" fill="none" stroke="currentColor"/></svg>Paywall Overlay</li>
      <li><svg viewBox="0 0 8 8"><rect x=".5" y=".5" width="7" height="7" fill="none" stroke="currentColor"/><path d="M3 .5v7" stroke="currentColor"/></svg>Navigation Shell</li>
    </ul>
  </aside>

  <h1 class="page-title">Mail-Log</h1>
  <p class="page-desc">Deep inspection of enterprise inbound and outbound traffic. Analysis based on Sentinel curator scoring.</p>
  <div class="btn" style="left:637px;top:83px;width:72px;height:19px;font-size:6.5px">⤓ Export Logs</div>
  <div class="btn btn--dark" style="left:716px;top:83px;width:74px;height:19px;font-size:6.5px">↻ Refresh Data</div>

  <div class="card" style="left:150px;top:123px;width:640px;height:55px;background:#131313">
    <span class="field-label" style="left:11px">DATE RANGE</span>
    <span class="field-label" style="left:145px">VERDICT</span>
    <span class="field-label" style="left:233px">SENDER / DOMAIN</span>
    <div class="field" style="left:11px;width:125px">▫ Oct 24, 2023 - Oct 31, 2023</div>
    <div class="field" style="left:146px;width:76px;justify-content:space-between">All Verdicts <svg width="6" height="6" viewBox="0 0 6 6"><path d="M1 2l2 2 2-2" stroke="#aaa" fill="none"/></svg></div>
    <div class="field" style="left:233px;width:315px;color:var(--dim)">Filter by address...</div>
    <div class="btn" style="left:558px;top:24px;width:72px;height:21px;font-size:6.5px">Apply Filters</div>
  </div>

  <div class="card" style="left:150px;top:191px;width:640px;height:258px">
    <table class="log-table">
      <colgroup><col style="width:69px"><col style="width:103px"><col style="width:104px"><col style="width:104px"><col style="width:103px"><col style="width:68px"><col style="width:65px"></colgroup>
      <thead><tr><th>S.No</th><th>Zeit</th><th>Absender</th><th>Empfänger</th><th>Betreff</th><th>Verdict</th><th>Score</th></tr></thead>
      <tbody>
        <tr><td>01</td><td>13.04.2026, 15:13</td><td>kontakt@beispiel.de</td><td>kontakt@beispiel.de</td><td>Invoice for March</td><td><span class="verdict v-ham">Ham <small>⌄</small></span></td><td>0.0 – 10.0</td></tr>
        <tr><td>02</td><td>14.04.2026, 09:45</td><td>kontakt@beispiel.de</td><td>kontakt@beispiel.de</td><td>Invoice for March</td><td><span class="verdict v-spam">Spam <small>⌄</small></span></td><td>0.0 – 10.0</td></tr>
        <tr><td>03</td><td>15.04.2026, 11:30</td><td>kontakt@beispiel.de</td><td>kontakt@beispiel.de</td><td>Invoice for March</td><td><span class="verdict v-phish">Phishing <small>⌄</small></span></td><td>8.5 – 10.0</td></tr>
        <tr><td>04</td><td>16.04.2026, 14:22</td><td>kontakt@beispiel.de</td><td>kontakt@beispiel.de</td><td>Invoice for March</td><td><span class="verdict v-virus">Virus <small>⌄</small></span></td><td>7.0 – 10.0</td></tr>
        <tr><td>05</td><td>17.04.2026, 08:55</td><td>kontakt@beispiel.de</td><td>kontakt@beispiel.de</td><td>Invoice for March</td><td><span class="verdict v-ham">Ham <small>⌄</small></span></td><td>9.0 – 10.0</td></tr>
        <tr><td>06</td><td>18.04.2026, 16:10</td><td>kontakt@beispiel.de</td><td>kontakt@beispiel.de</td><td>Invoice for March</td><td><span class="verdict v-spam">Spam <small>⌄</small></span></td><td>7.5 – 10.0</td></tr>
      </tbody>
    </table>
  </div>

  <div class="card" style="left:150px;top:462px;width:640px;height:36px;background:#131313;border-color:#1c1c1c">
    <div class="abs" style="left:13px;top:14px;font-size:5px;color:#bdbdbd">Showing 1-25 of 12,482 entries</div>
    <div class="pager"><span>Previous</span><span class="cur">1</span><span>2</span><span>3</span><span>Next</span></div>
  </div>
</section>

<!-- ================= QUARANTINE ================= -->
<section class="panel panel--quar">
  <header class="topbar">
    <div class="brand"><span class="brand-dot"></span>Mailbrook</div>
    <div class="greet"><h2>Guten Tag, Lena Maurer</h2><p>Beobachtungsmodus - Mails werden analysiert aber nicht blockiert</p></div>
    <div class="tools">
      <svg class="tool" viewBox="0 0 20 20"><circle cx="10" cy="10" r="9" fill="#eee"/><circle cx="6" cy="10" r="1.3" fill="#111"/><circle cx="10" cy="10" r="1.3" fill="#111"/><circle cx="14" cy="10" r="1.3" fill="#111"/></svg>
      <svg class="tool" viewBox="0 0 20 20"><path d="M5 15h10l-1.5-2V9a3.5 3.5 0 0 0-7 0v4z" fill="none" stroke="#eee" stroke-width="1.6"/><circle cx="15" cy="5" r="4" fill="var(--green)"/></svg>
      <div class="avatar" role="img" aria-label="Profilfoto des Benutzers"></div>
      <div class="user">Lena Maurer <svg width="6" height="6" viewBox="0 0 6 6"><path d="M1 2l2 2 2-2" stroke="#eee" fill="none"/></svg></div>
    </div>
  </header>
  <aside class="sidebar">
    <ul class="nav">
      <li><svg viewBox="0 0 8 8"><rect x="0" y="0" width="3" height="3" fill="currentColor"/><rect x="5" y="0" width="3" height="3" fill="currentColor"/><rect x="0" y="5" width="3" height="3" fill="currentColor"/><rect x="5" y="5" width="3" height="3" fill="currentColor"/></svg>Dashboard</li>
      <li><svg viewBox="0 0 8 8"><path d="M0 1h8M0 4h8M0 7h8" stroke="currentColor"/></svg>Mail-Log</li>
      <li class="is-active"><svg viewBox="0 0 8 8"><path d="M4 .5l3 1.2v2.6C7 6 5.5 7.2 4 7.6 2.5 7.2 1 6 1 4.3V1.7z" fill="none" stroke="currentColor"/></svg>Quarantine</li>
      <li><svg viewBox="0 0 8 8"><rect x=".5" y="1.5" width="7" height="5" fill="none" stroke="currentColor"/></svg>Mailbox Quota</li>
      <li><svg viewBox="0 0 8 8"><circle cx="4" cy="4" r="3" fill="none" stroke="currentColor"/><circle cx="4" cy="4" r="1" fill="currentColor"/></svg>Settings</li>
      <li><svg viewBox="0 0 8 8"><rect x="1.5" y="3.5" width="5" height="4" fill="none" stroke="currentColor"/><path d="M2.5 3.5V2a1.5 1.5 0 0 1 3 0v1.5" fill="none" stroke="currentColor"/></svg>Paywall Overlay</li>
      <li><svg viewBox="0 0 8 8"><rect x=".5" y=".5" width="7" height="7" fill="none" stroke="currentColor"/><path d="M3 .5v7" stroke="currentColor"/></svg>Navigation Shell</li>
    </ul>
  </aside>

  <h1 class="page-title">Quarantine</h1>
  <p class="page-desc">Manage intercepted communications. Your curated vault for suspicious activity requiring manual validation or systematic purge.</p>
  <div class="btn" style="left:720px;top:83px;width:70px;height:19px;font-size:6.5px">☰ Filter Vault</div>

  <div class="card" style="left:150px;top:123px;width:640px;height:29px;background:#131313;border-color:#1c1c1c">
    <div class="abs" style="left:13px;top:10px;display:flex;gap:10px;align-items:center;font-size:4.8px;letter-spacing:.08em;color:#cfcfcf">
      <span class="tool-item" style="color:var(--dim)"><span style="width:7px;height:7px;border:1px solid #555;border-radius:1px"></span>SELECT ALL</span>
      <span style="width:1px;height:10px;background:var(--line)"></span>
      <span class="tool-item">◎ RELEASE</span>
      <span class="tool-item">▭ BULK PURGE</span>
      <span class="tool-item">◇ MARK SAFE</span>
    </div>
    <div class="abs" style="right:13px;top:11px;font-size:4.5px;letter-spacing:.12em;color:var(--dim)">SHOWING 4 ITEMS IN CURATION</div>
  </div>

  <div class="card q-card" style="left:151px;top:165px;width:313px;height:142px">
    <div class="mail">kontakt@beispiel.de</div>
    <div class="pill v-phish">Phishing <small>⌄</small></div>
    <div class="rule" style="top:39px"></div>
    <div class="subj">Urgent: Reset Your Password Now!</div>
    <div class="meta"><span>18.04.2026, 10:31</span><span>9.2</span></div>
    <div class="rule" style="top:102px"></div>
    <span class="check" style="left:12px;top:116px"></span>
    <div class="btn" style="left:180px;top:111px;width:56px;height:20px;font-size:6.5px">Freigeben</div>
    <div class="btn btn--red" style="left:250px;top:111px;width:50px;height:20px;font-size:6.5px">Löschen</div>
  </div>
  <div class="card q-card" style="left:477px;top:165px;width:313px;height:142px">
    <div class="mail">kontakt@beispiel.de</div>
    <div class="pill v-ham">Ham <small>⌄</small></div>
    <div class="rule" style="top:39px"></div>
    <div class="subj">Invoice for March 2026</div>
    <div class="meta"><span>18.04.2026, 10:31</span><span>9.2</span></div>
    <div class="rule" style="top:102px"></div>
    <span class="check" style="left:12px;top:116px"></span>
    <div class="btn" style="left:180px;top:111px;width:56px;height:20px;font-size:6.5px">Freigeben</div>
    <div class="btn btn--red" style="left:250px;top:111px;width:50px;height:20px;font-size:6.5px">Löschen</div>
  </div>
  <div class="card q-card" style="left:151px;top:320px;width:313px;height:141px">
    <div class="mail">kontakt@beispiel.de</div>
    <div class="pill v-spam">Spam <small>⌄</small></div>
    <div class="rule" style="top:39px"></div>
    <div class="subj">Payment Failed – Action Required</div>
    <div class="meta"><span>18.04.2026, 10:31</span><span>9.2</span></div>
    <div class="rule" style="top:102px"></div>
    <span class="check" style="left:12px;top:116px"></span>
    <div class="btn" style="left:180px;top:111px;width:56px;height:20px;font-size:6.5px">Freigeben</div>
    <div class="btn btn--red" style="left:250px;top:111px;width:50px;height:20px;font-size:6.5px">Löschen</div>
  </div>
  <div class="card q-card" style="left:477px;top:320px;width:313px;height:141px">
    <div class="mail">kontakt@beispiel.de</div>
    <div class="pill v-virus">Virus <small>⌄</small></div>
    <div class="rule" style="top:39px"></div>
    <div class="subj">New Message from Support Team</div>
    <div class="meta"><span>18.04.2026, 10:31</span><span>9.2</span></div>
    <div class="rule" style="top:102px"></div>
    <span class="check" style="left:12px;top:116px"></span>
    <div class="btn" style="left:180px;top:111px;width:56px;height:20px;font-size:6.5px">Freigeben</div>
    <div class="btn btn--red" style="left:250px;top:111px;width:50px;height:20px;font-size:6.5px">Löschen</div>
  </div>
</section>

</div>
</body>
</html>
```